依頼詳細
■ デザイン

期間限定のキャンペーンメニュー(縦)です。

印刷掲示・印刷物配布・HPで使用します。

ファスティング(断食)をするためのリゾートホテルの宿泊客へむけたキャンペーンです。

テーマは、健康、デトックス、ダイエット、美しくなる

メインターゲットは、健康志向が高い女性、30歳~60歳

文字は大きく(50歳代が裸眼で見えるサイズ)

■使用する場所
ホテル内フロント・アロマルームで印刷物にラミネートをかけて掲示します
客室インフォメーションブックで印刷物を掲示します
HPに掲載します

■ 納品ファイル
JPG ai PDF

■添付ファイル
キャンペーン企画書
イメージ画像(必ずしも本画像が必須というわけではありません。お手持ちなどがありましたらご提案ください。)

■デザイン納期
4月上旬予定

■画像
お手持ちのものなど、無償使用できる画像でご提案ください。
場合により弊社所有の画像への入れ替えを提案することがあります。

■最下段には、2パターン店舗情報を記入してください。

■詳しくは企画書をご覧ください。ご不明点はメールでお問い合わせください

記載項目
サイズ
A4
ページ数
片面
希望イメージ
シンプル 複雑
単色 カラフル
暗い 明るい
日常 高級
遊び心 厳粛
未来的 伝統的
女性的 男性的
納品ファイル
• 高解像度JPG (.jpg)
• イラストレーター形式 (.ai)
■ 選んだ理由

本キャンペーンのイメージと、メニューの両方がとてもわかりやすく表現されていました。
1、2つのメニューの見やすい色と配置。
2、年齢層高い方にも文字サイズがほどよい。
3、本企画のテーマが表現されている。
4、季節感が感じられる。
5、シンプルななかにも柑橘が香り立つように盛り込まれている。
などが決め手となりました。

■ 提案者全員のお礼・コメント

この度は弊社コンペに多数ご応募くださいましてありがとうございました。とても素晴らしい作品が多く選出にはとても苦労をしました。また引き続きよろしくお願いいたします。

```html
<!DOCTYPE html>
<html lang="ja">
<head>
<meta charset="UTF-8">
<title>春限定 爽健アロマデトックス</title>
<link rel="stylesheet" href="https://fonts.googleapis.com/css2?family=M+PLUS+Rounded+1c:wght@500;700;800&family=Noto+Sans+JP:wght@400;500;700&display=swap">
<style>
:root{
  --bg-top:#eef7f1;
  --bg-bottom:#f7fbf4;
  --green:#5cb531;
  --green-dark:#3f8f22;
  --green-soft:#e6f3da;
  --teal:#1d9bb0;
  --teal-dark:#14798c;
  --blue:#3f9fd6;
  --blue-soft:#e1f0f9;
  --ink:#3a3a3a;
  --price:#2f8c1f;
  --price-blue:#2a7fbf;
  --white:#ffffff;
}
*{margin:0;padding:0;box-sizing:border-box}
html,body{width:846px;height:1200px;overflow:hidden}
body{
  font-family:"Noto Sans JP",sans-serif;color:var(--ink);
  background:linear-gradient(180deg,var(--bg-top) 0%,var(--white) 45%,var(--bg-bottom) 100%);
  position:relative;
}
.poster{position:relative;width:846px;height:1200px;overflow:hidden}
.hero-photo{
  position:absolute;left:0;top:0;width:360px;height:380px;
  background:radial-gradient(ellipse at 35% 40%,#f6e3d6 0%,#eed8c8 35%,#e4efe6 70%,rgba(238,247,241,0) 100%);
}
.leaf-deco{position:absolute;border-radius:50%}
.leaf-deco.top{right:0;top:0;width:300px;height:120px;background:radial-gradient(ellipse at 70% 20%,#cfe9b6 0%,rgba(207,233,182,0) 70%)}
.leaf-deco.mid{left:0;top:330px;width:280px;height:300px;background:radial-gradient(ellipse at 40% 50%,#d4ecbd 0%,rgba(212,236,189,0) 70%)}
.citrus{
  position:absolute;right:14px;top:430px;width:140px;height:130px;border-radius:50%;
  background:radial-gradient(circle at 45% 50%,#fbe7a4 0%,#f6cf64 55%,rgba(246,207,100,0) 75%);
}
.season-badge{
  position:absolute;left:370px;top:70px;width:100px;height:100px;border-radius:50%;
  background:var(--green);color:var(--white);
  font-family:"M PLUS Rounded 1c",sans-serif;font-weight:800;font-size:30px;line-height:1.05;
  display:flex;flex-direction:column;align-items:center;justify-content:center;
}
.title{position:absolute;font-family:"M PLUS Rounded 1c",sans-serif;font-weight:800;letter-spacing:4px}
.title.main{left:490px;top:50px;font-size:96px;color:var(--green);line-height:1}
.title.aroma{left:480px;top:170px;font-size:74px;color:var(--teal);line-height:1}
.title.detox{left:400px;top:250px;font-size:82px;color:var(--teal);line-height:1;transform:rotate(-3deg);transform-origin:left center}
.campaign{
  position:absolute;left:40px;top:335px;width:240px;height:240px;border-radius:50%;
  background:radial-gradient(circle,#ffffff 60%,#e7f4dc 100%);
  border:3px solid var(--teal);
  display:flex;flex-direction:column;align-items:center;justify-content:center;text-align:center;
}
.campaign-label{
  background:var(--teal);color:var(--white);font-family:"M PLUS Rounded 1c",sans-serif;font-weight:700;
  font-size:22px;padding:4px 22px;border-radius:20px;margin-bottom:8px;
}
.campaign-note{font-size:13px;color:var(--teal-dark)}
.campaign-offer{display:flex;align-items:center;gap:6px;margin:4px 0}
.campaign-tag{background:var(--teal);color:var(--white);font-size:14px;font-weight:700;line-height:1.1;padding:4px 5px;border-radius:4px}
.campaign-price{font-family:"M PLUS Rounded 1c",sans-serif;font-weight:800;font-size:52px;color:var(--teal-dark);line-height:1}
.campaign-price small{font-size:26px}
.intro{
  position:absolute;left:330px;top:425px;width:480px;
  font-size:16px;font-weight:500;line-height:1.85;text-align:center;color:var(--ink);
  white-space:nowrap;
}
.menu{position:absolute;top:610px;width:380px}
.menu.left{left:30px}
.menu.right{left:436px}
.menu-head{
  color:var(--white);font-family:"M PLUS Rounded 1c",sans-serif;font-weight:800;font-size:27px;
  text-align:center;padding:8px 0;border-radius:28px;letter-spacing:1px;
}
.left .menu-head{background:var(--green)}
.right .menu-head{background:var(--blue)}
.menu-desc{font-size:16px;line-height:1.6;text-align:center;margin:14px 0 10px;font-weight:500}
.menu-body{position:relative;padding-left:40px}
.course-label{
  position:absolute;left:0;top:30px;bottom:0;width:30px;border-radius:6px;
  writing-mode:vertical-rl;font-size:17px;font-weight:700;letter-spacing:6px;
  display:flex;align-items:center;justify-content:center;color:var(--white);
}
.left .course-label{background:var(--green)}
.right .course-label{background:var(--blue)}
.recommend{font-size:13px;font-weight:700;margin-left:20px;margin-bottom:4px}
.left .recommend{color:var(--green-dark)}
.right .recommend{color:var(--price-blue)}
.price-row{
  display:flex;align-items:center;height:62px;margin-bottom:6px;border-radius:8px;padding:0 12px 0 0;
}
.left .price-row{background:var(--green-soft)}
.right .price-row{background:var(--blue-soft)}
.duration{
  width:82px;height:46px;border-radius:6px;margin-left:6px;color:var(--white);
  font-family:"M PLUS Rounded 1c",sans-serif;font-weight:800;font-size:24px;
  display:flex;align-items:center;justify-content:center;
}
.left .duration{background:var(--green)}
.right .duration{background:var(--blue)}
.dash{flex:0 0 24px;text-align:center;font-size:20px;color:#999}
.amount{margin-left:auto;font-family:"M PLUS Rounded 1c",sans-serif;font-weight:800;font-size:40px;letter-spacing:1px}
.amount small{font-size:20px;margin-left:2px}
.left .amount{color:var(--price)}
.right .amount{color:var(--price-blue)}
.menu-note{font-size:12px;line-height:1.6;text-align:center;margin-top:10px;color:#555}
.footer{
  position:absolute;left:0;bottom:0;width:846px;height:86px;background:var(--teal);color:var(--white);
  display:flex;align-items:center;justify-content:space-between;padding:0 28px;
}
.footer-left .room{display:flex;align-items:center;gap:14px}
.room-name{font-family:"M PLUS Rounded 1c",sans-serif;font-weight:800;font-size:30px}
.room-place{background:var(--white);color:var(--teal-dark);font-size:15px;font-weight:700;padding:2px 10px;border-radius:4px}
.hours{font-size:15px;margin-top:4px}
.footer-right{text-align:center}
.contact{background:var(--white);color:var(--teal-dark);font-size:18px;font-weight:700;padding:4px 16px;border-radius:4px}
.reserve{font-size:13px;margin-top:6px}
</style>
</head>
<body>
<main class="poster">
  <div class="hero-photo" role="img" aria-label="目を閉じてリラックスする女性のアロマトリートメント写真"></div>
  <div class="leaf-deco top" role="img" aria-label="若葉のあしらい"></div>
  <div class="leaf-deco mid" role="img" aria-label="若葉のあしらい"></div>
  <div class="citrus" role="img" aria-label="グレープフルーツとダイダイの輪切り"></div>

  <div class="season-badge"><span>春</span><span>限定</span></div>
  <h1>
    <span class="title main">爽健</span>
    <span class="title aroma">アロマ</span>
    <span class="title detox">デトックス</span>
  </h1>

  <section class="campaign">
    <div class="campaign-label">キャンペーン</div>
    <p class="campaign-note">期間中のご予約で</p>
    <div class="campaign-offer">
      <span class="campaign-tag">通常<br>料金</span>
      <span class="campaign-price">500<small>円</small></span>
    </div>
    <p class="campaign-note">各コースより割引いたします</p>
  </section>

  <p class="intro">伊豆特産ダイダイとグレープフルーツオイルで<br>溜った毒素を分解してリンパ活性トリートメントで<br>デトックスをうながします。</p>

  <section class="menu left">
    <h2 class="menu-head">利尿デトックスボディ</h2>
    <p class="menu-desc">むくみや倦怠感を軽くするために、<br>余分な水分の排出をサポートします。</p>
    <div class="menu-body">
      <div class="course-label">コース・価格</div>
      <p class="recommend">おすすめ</p>
      <div class="price-row"><span class="duration">45分</span><span class="dash">…</span><span class="amount">6,300<small>円</small></span></div>
      <div class="price-row"><span class="duration">60分</span><span class="dash">…</span><span class="amount">8,470<small>円</small></span></div>
      <div class="price-row"><span class="duration">90分</span><span class="dash">…</span><span class="amount">12,540<small>円</small></span></div>
      <div class="price-row"><span class="duration">120分</span><span class="dash">…</span><span class="amount">15,730<small>円</small></span></div>
    </div>
    <p class="menu-note">グレープフルーツオイルに含まれるリモネン成分が<br>余分な水分の排出をうながします。<br>香り成分が爽快なリフレッシュをサポートします。</p>
  </section>

  <section class="menu right">
    <h2 class="menu-head">爽快デトックスボディ</h2>
    <p class="menu-desc">腸を活性化することで、<br>老廃物の排出力を高めます。</p>
    <div class="menu-body">
      <div class="course-label">コース・価格</div>
      <p class="recommend">おすすめ</p>
      <div class="price-row"><span class="duration">45分</span><span class="dash">…</span><span class="amount">6,300<small>円</small></span></div>
      <div class="price-row"><span class="duration">60分</span><span class="dash">…</span><span class="amount">8,470<small>円</small></span></div>
      <div class="price-row"><span class="duration">90分</span><span class="dash">…</span><span class="amount">12,540<small>円</small></span></div>
      <div class="price-row"><span class="duration">120分</span><span class="dash">…</span><span class="amount">15,730<small>円</small></span></div>
    </div>
    <p class="menu-note">伊豆ダイダイの柑橘成分が腸を刺激して巡りを促します。<br>ペパーミントとジンジャーを配合し<br>すっきり軽やかな体をサポートします。</p>
  </section>

  <footer class="footer">
    <div class="footer-left">
      <div class="room"><span class="room-name">アロマルーム</span><span class="room-place">東館1階にございます</span></div>
      <p class="hours">営業時間 ▶15:00〜22:00　受付時間 ▶15:00〜18:00</p>
    </div>
    <div class="footer-right">
      <p class="contact">お問合せはフロントで承ります</p>
      <p class="reserve">（全コース完全予約制）</p>
    </div>
  </footer>
</main>
</body>
</html>
```